Business Card Design - Law Firm

We are a boutique law firm located near the beach in Manly, Australia. We have recently had a new logo designed and are revamping our business cards with the new logo.

We have recently had a business card design done for us but are not entirely happy with it. We are looking for something modern, simplistic but striking. We would like to see multiple designs.

We have attached a word document which includes our new logo and the current business card design which we are looking at moving away from.

We would like the business cards to be double sided. We would like the design to include something which we can print in gloss colour when we send it to the business card printers.

```html
<!DOCTYPE html>
<html lang="en">
<head>
<meta charset="utf-8">
<title>Harrow &amp; Partners – Business Card</title>
<link href="https://fonts.googleapis.com/css2?family=Montserrat:wght@400;500;600;700&display=swap" rel="stylesheet">
<style>
  :root {
    --stage: #1c1c1c;
    --card-dark: #262626;
    --card-white: #ffffff;
    --ink-white: #f2f2f2;
    --ink-dark: #2b2b2b;
    --accent-blue: #6f86cf;
    --accent-gold: #c9b27a;
    --arc-black: #151515;
  }
  * { margin: 0; padding: 0; box-sizing: border-box; }
  html, body {
    width: 1200px; height: 900px; overflow: hidden;
    background: var(--stage);
    font-family: "Montserrat", sans-serif;
  }
  .canvas { position: relative; width: 1200px; height: 900px; }
  .card {
    position: absolute; left: 270px; width: 660px; height: 377px;
    background: var(--card-dark);
    box-shadow: 0 12px 30px rgba(0,0,0,.55);
    overflow: hidden;
  }
  .card-back { top: 50px; }
  .card-front { top: 470px; }

  /* back */
  .brand-block {
    position: absolute; left: 0; right: 0; top: 150px;
    text-align: center; color: var(--ink-white);
  }
  .brand-mark {
    width: 12px; height: 12px; border-radius: 50%;
    background: var(--accent-blue); margin: 0 auto 14px;
  }
  .brand-name { font-size: 27px; font-weight: 600; letter-spacing: 2px; white-space: nowrap; }
  .brand-tag { font-size: 13px; letter-spacing: 13px; margin-top: 6px; padding-left: 13px; }

  /* front */
  .front-art { position: absolute; inset: 0; }
  .gold-tick {
    position: absolute; left: 28px; top: 50px; width: 5px; height: 34px;
    background: var(--accent-gold);
  }
  .person { position: absolute; left: 52px; top: 48px; }
  .person-name { font-size: 27px; font-weight: 600; color: var(--accent-blue); }
  .person-role { font-size: 15px; color: var(--ink-white); margin-top: -2px; }
  .address {
    position: absolute; left: 40px; top: 138px; font-style: normal;
    font-size: 16px; line-height: 21px; color: var(--ink-white);
  }
  .contacts {
    position: absolute; left: 22px; top: 232px; list-style: none;
    font-size: 17px; line-height: 28px; color: var(--ink-white);
  }
  .contacts li { display: flex; align-items: center; gap: 12px; }
  .contacts svg { width: 16px; height: 16px; fill: var(--accent-blue); flex: none; }
  .front-brand {
    position: absolute; left: 476px; top: 168px; width: 174px;
    text-align: center; color: var(--ink-dark);
  }
  .front-brand .brand-mark { margin-bottom: 12px; width: 14px; height: 14px; }
  .front-brand .brand-name { font-size: 15px; letter-spacing: .5px; }
  .front-brand .brand-tag { font-size: 9px; letter-spacing: 8px; padding-left: 8px; margin-top: 4px; }
</style>
</head>
<body>
<main class="canvas">
  <section class="card card-back" aria-label="Card back">
    <div class="brand-block">
      <div class="brand-mark"></div>
      <div class="brand-name">Harrow &amp; Partners</div>
      <div class="brand-tag">LAWYERS</div>
    </div>
  </section>

  <section class="card card-front" aria-label="Card front">
    <svg class="front-art" viewBox="0 0 660 377" aria-hidden="true">
      <path d="M660 0 H575 A210 210 0 0 0 552 377 H660 Z" fill="var(--card-white)"/>
      <path d="M525 30 A210 210 0 0 0 510 330" fill="none" stroke="var(--arc-black)" stroke-width="9" stroke-linecap="round"/>
    </svg>
    <span class="gold-tick"></span>
    <div class="person">
      <div class="person-name">Megan Tolley</div>
      <div class="person-role">Practice Manager</div>
    </div>
    <address class="address">
      Suite 4, 12 Pier Lane<br>COVEWOOD NSW 2190
    </address>
    <ul class="contacts">
      <li><svg viewBox="0 0 24 24"><path d="M6.6 10.8a15 15 0 0 0 6.6 6.6l2.2-2.2c.3-.3.7-.4 1-.2 1.1.4 2.3.6 3.6.6.6 0 1 .4 1 1V20c0 .6-.4 1-1 1A17 17 0 0 1 3 4c0-.6.4-1 1-1h3.5c.6 0 1 .4 1 1 0 1.3.2 2.5.6 3.6.1.3 0 .7-.2 1z"/></svg>(02) 9041 7368</li>
      <li><svg viewBox="0 0 24 24"><path d="M2 5h20v14H2z" fill="var(--accent-blue)"/><path d="M3 6l9 7 9-7" fill="none" stroke="var(--card-dark)" stroke-width="1.5"/></svg>megan.tolley@covewoodlaw.com.au</li>
      <li><svg viewBox="0 0 24 24"><circle cx="12" cy="12" r="10"/><path d="M2 12h20M12 2c3 3 3 17 0 20M12 2c-3 3-3 17 0 20" fill="none" stroke="var(--card-dark)" stroke-width="1.5"/></svg>www.harrowandpartners.com.au</li>
    </ul>
    <div class="front-brand">
      <div class="brand-mark"></div>
      <div class="brand-name">Harrow &amp; Partners</div>
      <div class="brand-tag">LAWYERS</div>
    </div>
  </section>
</main>
</body>
</html>
```